Stationery Design Project

We are a start up wine business based in Sydney Australia. We already have a logo and are in the process of completing our website. We require our logo to be cleverly and artfully incorporated into our stationary requirements. Which will initially begin with a company letter head.
As we desire consistency across our brand, we will also be wanting to develop banner advertisements and brochure with the same "look".
If outstanding we move design brief to banner advertisement for web and banner of the website itself.
Target Market(s)
Older wealthy predominantly male demographic
Industry/Entity Type
Business
Look and feel

```html
<!DOCTYPE html>
<html lang="en">
<head>
<meta charset="utf-8">
<title>Heritage Cellars — Business Card</title>
<link rel="stylesheet" href="https://fonts.googleapis.com/css2?family=Questrial&family=Tinos&display=swap">
<style>
  :root {
    --stage: #4a4a4c;
    --card-light: #a3a3a6;
    --card-dark: #222122;
    --ink-dark: #1e1e1f;
    --ink-light: #f2f2f2;
    --ink-muted: #7a7a7a;
    --rule: #8a8a8a;
  }
  * { margin: 0; padding: 0; box-sizing: border-box; }
  html, body { width: 1200px; height: 628px; overflow: hidden; }
  body {
    background: var(--stage);
    position: relative;
    font-family: "Questrial", sans-serif;
  }
  .card {
    position: absolute;
    top: 182px;
    width: 442px;
    height: 252px;
    border-radius: 14px;
    overflow: hidden;
  }
  .card--front { left: 130px; background: var(--card-light); }
  .card--back { left: 610px; background: var(--card-dark); }

  .front-url {
    position: absolute;
    left: 28px;
    top: 126px;
    transform: translate(-50%, -50%) rotate(-90deg);
    transform-origin: center;
    margin-left: 14px;
    font-family: "Tinos", serif;
    font-size: 13px;
    letter-spacing: 1.5px;
    color: var(--ink-dark);
    white-space: nowrap;
  }
  .brand {
    position: absolute;
    right: 26px;
    top: 108px;
    display: flex;
    align-items: center;
    gap: 10px;
    color: var(--ink-dark);
    font-size: 22px;
    letter-spacing: 0.5px;
  }
  .brand-dot {
    width: 14px; height: 14px;
    border-radius: 50%;
    background: var(--ink-dark);
  }

  .holder-name {
    position: absolute;
    left: 20px; top: 56px;
    color: var(--ink-light);
    font-size: 20px;
    letter-spacing: 1.2px;
  }
  .holder-role {
    position: absolute;
    left: 20px; top: 83px;
    color: var(--ink-light);
    font-size: 17px;
    letter-spacing: 1px;
  }
  .address {
    position: absolute;
    left: 20px; top: 184px;
    font-family: "Tinos", serif;
    font-size: 14px;
    line-height: 16px;
    color: var(--ink-muted);
  }
  .divider {
    position: absolute;
    left: 226px; top: 148px;
    width: 1px; height: 80px;
    background: var(--rule);
  }
  .contacts {
    position: absolute;
    left: 252px; top: 150px;
    list-style: none;
  }
  .contacts li {
    display: flex;
    align-items: center;
    gap: 14px;
    height: 20.5px;
    font-family: "Tinos", serif;
    font-size: 15px;
    color: var(--ink-muted);
  }
  .contacts svg { width: 13px; height: 13px; flex: none; }
</style>
</head>
<body>
  <section class="card card--front">
    <p class="front-url">www.heritagecellars.au</p>
    <div class="brand">
      <span class="brand-dot"></span>
      <span class="brand-name">Heritage Cellars</span>
    </div>
  </section>

  <section class="card card--back">
    <h1 class="holder-name">DORIAN HALBROOK</h1>
    <p class="holder-role">CEO</p>
    <address class="address">
      412 Harbour Row<br>
      Kingsford, NSW<br>
      2032
    </address>
    <span class="divider"></span>
    <ul class="contacts">
      <li>
        <svg viewBox="0 0 16 16" fill="none" stroke="#7a7a7a" stroke-width="1.4"><path d="M2 6c3-4 9-4 12 0l-2 1.5-1.5-1.5h-5L4 7.5z"/><rect x="4" y="9" width="8" height="5" rx="1"/></svg>
        <span>02-9481-3360</span>
      </li>
      <li>
        <svg viewBox="0 0 16 16" fill="none" stroke="#7a7a7a" stroke-width="1.4"><rect x="4" y="2" width="8" height="4"/><rect x="2" y="6" width="12" height="5"/><rect x="4" y="10" width="8" height="4"/></svg>
        <span>02-9481-3360</span>
      </li>
      <li>
        <svg viewBox="0 0 16 16" fill="none" stroke="#7a7a7a" stroke-width="1.4"><rect x="1.5" y="3.5" width="13" height="9"/><path d="M1.5 3.5 8 9l6.5-5.5"/></svg>
        <span>info@heritagecellars.au</span>
      </li>
      <li>
        <svg viewBox="0 0 16 16" fill="none" stroke="#7a7a7a" stroke-width="1.4"><circle cx="8" cy="8" r="6"/><ellipse cx="8" cy="8" rx="2.5" ry="6"/><path d="M2 8h12"/></svg>
        <span>www.heritagecellars.au</span>
      </li>
    </ul>
  </section>
</body>
</html>
```